Brandt Family Motto/Mission Statement

We are creating a poster to be hung in our home with several purpose statements for our family (last name Brandt, and "The Brandt Family" should be included in the poster prominently). The text that we want included is in the attached file.

Our kids range in age from 8 to 17, so we are looking for something that is homey and cheerful, but fairly bold and oriented to older kids (and not so much younger kids).

I've attached a couple of example poster/statements that we generally like. Overall color scheme could include blues and greens and possibly some brown.

Anticipated size of this poster would be 18"x24" with a portrait orientation.

```html
<!DOCTYPE html>
<html lang="en">
<head>
<meta charset="utf-8">
<title>The Brandt Family</title>
<link rel="stylesheet" href="https://fonts.googleapis.com/css2?family=Oswald:wght@400;500;600;700&family=Playfair+Display:ital,wght@1,700;1,900&family=Arvo:wght@400;700&display=swap">
<style>
  :root {
    --paper-light: #e4e5e3;
    --paper-mid: #d3d5d3;
    --paper-edge: #b9bcbb;
    --slate: #44596a;
    --navy: #1c2a38;
    --ink: #111a22;
    --ornament: #3f5466;
  }
  * { margin: 0; padding: 0; box-sizing: border-box; }
  html, body {
    width: 900px;
    height: 1200px;
    overflow: hidden;
  }
  body {
    background: var(--paper-mid);
  }
  .poster {
    position: relative;
    width: 900px;
    height: 1200px;
    background: radial-gradient(ellipse at 50% 45%, var(--paper-light) 0%, var(--paper-mid) 60%, var(--paper-edge) 100%);
    overflow: hidden;
  }
  .ornament {
    position: absolute;
    left: 50%;
    transform: translateX(-50%);
    width: 260px;
    height: 62px;
    border-radius: 31px;
    background: linear-gradient(90deg, transparent 0%, var(--ornament) 30%, var(--ornament) 70%, transparent 100%);
    opacity: 0.55;
  }
  .ornament--top { top: 26px; }
  .ornament--bottom { top: 1012px; }

  .line {
    position: absolute;
    left: 0;
    width: 100%;
    text-align: center;
    white-space: nowrap;
    line-height: 1;
    transform: translateY(-50%);
  }
  .title {
    top: 180px;
    font-family: "Oswald", sans-serif;
    font-weight: 600;
    font-size: 104px;
    letter-spacing: 3px;
    color: var(--slate);
  }
  .script {
    font-family: "Playfair Display", serif;
    font-style: italic;
    font-weight: 900;
    color: var(--navy);
  }
  .caps {
    font-family: "Oswald", sans-serif;
    font-weight: 500;
    text-transform: uppercase;
    color: var(--slate);
  }
  .slab {
    font-family: "Arvo", serif;
    font-weight: 700;
    color: var(--ink);
  }
  .learn { top: 264px; font-size: 52px; }
  .look { top: 324px; font-size: 48px; letter-spacing: 1px; }
  .through { top: 378px; font-size: 48px; letter-spacing: 1px; }
  .through .emphasis { font-weight: 700; font-size: 62px; }
  .kindness { top: 444px; font-size: 42px; color: var(--navy); }
  .kindness .emphasis { font-weight: 700; }
  .adventure { top: 510px; font-size: 46px; }
  .adventure .emphasis { font-size: 54px; color: var(--slate); }
  .experiences { top: 570px; font-size: 48px; }
  .fit { top: 639px; font-size: 56px; }
  .brightened { top: 714px; font-size: 56px; letter-spacing: 1px; }
  .humor { top: 786px; font-size: 72px; font-weight: 700; letter-spacing: 2px; }
  .right { top: 876px; font-size: 58px; text-transform: uppercase; font-weight: 400; }
  .watching { top: 951px; font-size: 44px; text-transform: uppercase; font-weight: 400; }
</style>
</head>
<body>
  <main class="poster">
    <div class="ornament ornament--top" role="img" aria-label="Decorative scroll flourish"></div>

    <h1 class="line title">THE BRANDT FAMILY</h1>

    <p class="line script learn">We love to learn new things.</p>
    <p class="line caps look">We look at life</p>
    <p class="line caps through">Through a <span class="emphasis">positive</span> lens.</p>
    <p class="line caps kindness"><span class="emphasis">Kindness</span> guides our words and deeds.</p>
    <p class="line script adventure">We create <span class="emphasis">adventure</span> and</p>
    <p class="line script experiences">choose experiences over things.</p>
    <p class="line slab fit">We commit to be fit.</p>
    <p class="line caps brightened">Our days are brightened by</p>
    <p class="line caps humor">A sense of humor.</p>
    <p class="line slab right">We do what is right</p>
    <p class="line slab watching">Even when no one is watching.</p>

    <div class="ornament ornament--bottom" role="img" aria-label="Decorative scroll flourish"></div>
  </main>
</body>
</html>
```